Corvane Health a direct primary care practice needs a beautiful and customer friendly website

We need a website to showcase our new medical practice. We want to enhance the customer experience and make it easy to navigate to the desired page by placing pillar pages on the home screen. the website needs to be clean and bright.

Target Market(s)

Uninsured, Small businesses that can't afford to offer employees insurance.

Industry/Entity Type

Healthcare

Coding

Coded - Design and coding required

Font styles to use
Serif
Sans Serif

Colors
0592cd
3377b5
0355a3
9bcb3c
acd136

Requirements
Must have
• Must be user friendly, must have pillar pages to help boost SEO ranking, clean and bright, must be close to the in colors to the attached logo.

Content will be very similar to www.brindlecare.example
Nice to have
• Clean and easy to read font

```html
<!DOCTYPE html>
<html lang="en">
<head>
<meta charset="utf-8">
<title>Corvane Health</title>
<link href="https://fonts.googleapis.com/css2?family=Lato:wght@400;700;900&display=swap" rel="stylesheet">
<style>
:root{
  --navy:#0f3f8f;
  --blue:#1a6bb8;
  --sky:#0592cd;
  --mid:#3377b5;
  --deep:#0355a3;
  --green:#8cc63f;
  --lime:#acd136;
  --ink:#2b2b2b;
  --body:#444;
  --gray:#f3f3f3;
}
*{box-sizing:border-box;margin:0;padding:0}
html,body{width:1200px;height:3434px;overflow:hidden}
body{font-family:'Lato',sans-serif;color:var(--ink);background:#fff;position:relative}
.abs{position:absolute}
.brand{font-family:'Lato',sans-serif;font-weight:700;color:var(--navy);display:flex;align-items:center;gap:8px}
.brand .dot{width:12px;height:12px;border-radius:50%;background:var(--green)}
/* header */
.site-header{top:0;left:0;width:1200px;height:116px;background:#fff}
.site-header .brand{left:80px;top:45px;font-size:28px}
.nav{left:316px;top:55px;display:flex;gap:0;font-size:12.5px;font-weight:700;text-transform:uppercase}
.nav a{color:#222;text-decoration:none;margin-right:35px}
.nav a.active{color:var(--deep)}
.join{left:1040px;top:43px;width:87px;height:39px;background:var(--green);color:#fff;font-size:12.5px;font-weight:700;display:flex;align-items:center;justify-content:center}
/* hero */
.hero{top:116px;left:0;width:1200px;height:591px;overflow:hidden}
.hero-photo{position:absolute;inset:0;background:linear-gradient(110deg,#b7c9dd 0%,#e8eef6 55%,#c9d6e6 100%)}
.hero-panel{position:absolute;inset:0}
.hero h1{left:73px;top:196px;color:#fff;font-size:54px;font-weight:900;letter-spacing:.5px}
.hero p{left:73px;top:258px;color:#fff;font-size:19px;line-height:28px}
.btn{background:var(--green);color:#fff;font-weight:700;display:flex;align-items:center;justify-content:center;font-size:19px}
.hero .btn{left:73px;top:331px;width:180px;height:54px}
.dots{left:73px;top:531px;display:flex;gap:8px}
.dots i{width:12px;height:12px;border-radius:50%;background:#fff}
.dots i:first-child{background:var(--green)}
/* welcome */
.welcome-title{top:756px;left:0;width:1200px;text-align:center;color:var(--deep);font-size:34px;font-weight:900}
.tabs{top:824px;left:475px;display:flex;font-size:17px;font-weight:700}
.tabs span{padding:0 18px 10px 17px}
.tabs .on{color:var(--sky);border-bottom:3px solid var(--sky);width:120px}
.video{left:75px;top:892px;width:512px;height:326px;background:linear-gradient(120deg,#dfe7ee,#c7d3de 60%,#9aa9b7)}
.play{left:281px;top:1005px}
.intro h2{left:614px;top:884px;width:500px;color:var(--sky);font-size:21px;line-height:31px;font-weight:900;text-transform:uppercase}
.intro p{left:614px;top:958px;width:506px;font-size:14px;line-height:27.7px;color:var(--body)}
.intro .btn{left:615px;top:1163px;width:180px;height:55px}
/* services */
.services{top:1289px;left:0;width:1200px;height:906px;background:linear-gradient(30deg,#0d3e94 0%,#2f6f8a 35%,#5a9a5a 65%,#8cc63f 100%)}
.services h2{top:84px;width:1200px;text-align:center;color:#fff;font-size:33px;font-weight:900}
.svc{width:330px;color:#fff;text-align:center}
.svc .ph{height:213px}
.svc h3{margin-top:19px;font-size:20px;font-weight:700}
.svc p{margin-top:8px;font-size:14px;line-height:26px;color:#eef}
/* pillars */
.pillar{top:2247px;width:242px;height:151px;background:linear-gradient(180deg,#1a72c2,#0d3f8f);color:#fff;font-size:18px;font-weight:700;text-align:center}
.pillar svg{display:block;margin:28px auto 16px}
/* blog */
.blog{top:2467px;left:0;width:1200px;height:476px;background:var(--gray)}
.blog h2{left:73px;top:44px;font-size:33px;font-weight:700;color:#444}
.arrows{left:1080px;top:50px}
.post{top:112px;width:331px}
.post .ph{height:180px}
.post h3{margin-top:18px;color:var(--deep);font-size:20px;font-weight:700}
.post p{margin-top:6px;font-size:13px;line-height:23px;color:#333}
.post p a{color:var(--green);text-decoration:none}
/* subscribe */
.subscribe{top:2943px;left:0;width:1200px;height:83px;background:linear-gradient(90deg,#8cc63f 0%,#3a8070 45%,#0d3e94 100%);color:#fff}
.subscribe .lbl{left:75px;top:29px;font-size:18px;font-weight:700}
.subscribe .field{left:255px;top:22px;width:255px;height:38px;background:#fff;color:#333;font-size:11px;font-weight:700;padding:13px 10px}
.subscribe .go{left:518px;top:22px;width:102px;height:38px;background:#222;color:#fff;font-size:11px;font-weight:700;display:flex;align-items:center;justify-content:center}
.subscribe .follow{left:794px;top:29px;font-size:18px;font-weight:700}
.social{left:918px;top:28px;display:flex;gap:28px}
.social i{width:20px;height:20px;border-radius:50%;background:#fff;display:block}
/* footer */
.footer .brand{left:76px;top:3128px;font-size:28px}
.copy{left:76px;top:3180px;font-size:12px;line-height:22px;color:#222}
.fcol h4{font-size:16px;font-weight:700;color:#333;margin-bottom:8px}
.fcol li{list-style:none;font-size:14px;line-height:29.6px;color:#333}
.contact li{display:flex;gap:16px;align-items:flex-start}
.contact svg{flex:none;margin-top:7px}
</style>
</head>
<body>

<header class="site-header abs">
  <div class="brand abs"><span class="dot"></span>Corvane Health</div>
  <nav class="nav abs">
    <a class="active">Home</a><a>About Us</a><a>Services</a><a>Employers</a><a>Pricing</a><a>FAQ'S</a><a>Blog</a><a>Contact Us</a>
  </nav>
  <div class="join abs">JOIN US</div>
</header>

<section class="hero abs">
  <div class="hero-photo" role="img" aria-label="Smiling doctor listening to a young patient with a stethoscope, eye chart in background"></div>
  <svg class="hero-panel" width="1200" height="591" viewBox="0 0 1200 591">
    <polygon points="0,0 495,0 615,591 0,591" fill="#1f5fb3" opacity=".82"/>
  </svg>
  <h1 class="abs">CORVANE HEALTH</h1>
  <p class="abs">Sed sit amet sollicitudin lacus, a malesuada lorem<br>Sed eleifend efficitur odio id rutrum</p>
  <div class="btn abs">READ MORE</div>
  <div class="dots abs"><i></i><i></i><i></i><i></i></div>
</section>

<h2 class="welcome-title abs">WELCOME TO CORVANE HEALTH</h2>
<div class="tabs abs"><span class="on">OVERVIEW</span><span>DIFFERENCE</span></div>
<div class="video abs" role="img" aria-label="Doctor talking with an elderly patient in a consultation room"></div>
<svg class="play abs" width="100" height="100" viewBox="0 0 100 100"><circle cx="50" cy="50" r="45" fill="none" stroke="#fff" stroke-width="7"/><polygon points="38,28 38,72 74,50" fill="#fff"/></svg>
<div class="intro">
  <h2 class="abs">Enjoy more personal medical care in Huntington Beach</h2>
  <p class="abs">Lorem ipsum dolor sit amet, consectetur adipiscing elit ultricies lectus. Donec porttitor, nisl ac pellentesque faucibus, ante ante imperdiet augue, ut sodales sapien metus et mauris. Donec finibus convallis viverra turpis, vehicula quis metus vitae, vulputate facilisis metus. Proin porttitor quam nec elit viverra tincidunt vel vitae massa maecenas aliquet placerat eros et semper.</p>
  <div class="btn abs">READ MORE</div>
</div>

<section class="services abs">
  <h2 class="abs">OUR SERVICES</h2>
  <div class="svc abs" style="left:75px;top:158px"><div class="ph" role="img" aria-label="Doctor examining a woman patient" style="background:linear-gradient(120deg,#e6ecef,#b9c6cf)"></div><h3>General Health Visits</h3><p>Lorem ipsum dolor sit amet, consectetur<br>adipiscing elit ultricies.</p></div>
  <div class="svc abs" style="left:434px;top:158px"><div class="ph" role="img" aria-label="Senior woman on a video call with a doctor on a tablet" style="background:linear-gradient(120deg,#e3dfd8,#b7b0a4)"></div><h3>Telemedicine</h3><p>Lorem ipsum dolor sit amet, consectetur<br>adipiscing elit ultricies.</p></div>
  <div class="svc abs" style="left:796px;top:158px"><div class="ph" role="img" aria-label="Clinician reviewing scan images on monitors" style="background:linear-gradient(120deg,#3c5878,#8aa0b8)"></div><h3>Medical Imaging</h3><p>Lorem ipsum dolor sit amet, consectetur<br>adipiscing elit ultricies.</p></div>
  <div class="svc abs" style="left:75px;top:511px"><div class="ph" role="img" aria-label="Nurse giving a vaccine to a masked man" style="background:linear-gradient(120deg,#6d6a66,#c9c1b6)"></div><h3>Vaccinations</h3><p>Lorem ipsum dolor sit amet, consectetur<br>adipiscing elit ultricies.</p></div>
  <div class="svc abs" style="left:434px;top:511px"><div class="ph" role="img" aria-label="Scientists working in a laboratory" style="background:linear-gradient(120deg,#2f4a63,#a6bac9)"></div><h3>Additional Lab Testing</h3><p>Lorem ipsum dolor sit amet, consectetur<br>adipiscing elit ultricies.</p></div>
  <div class="svc abs" style="left:796px;top:511px"><div class="ph" role="img" aria-label="Doctor examining an older man's shoulder" style="background:linear-gradient(120deg,#2f5b9c,#d8dde3)"></div><h3>Specialized Treatments</h3><p>Lorem ipsum dolor sit amet, consectetur<br>adipiscing elit ultricies.</p></div>
</section>

<div class="pillar abs" style="left:75px">
  <svg width="46" height="46" viewBox="0 0 46 46"><rect x="4" y="20" width="9" height="22" fill="#fff"/><path d="M16 20 L24 4 Q30 4 28 16 L40 16 Q44 18 42 24 L38 40 Q36 42 32 42 L16 42 Z" fill="#fff"/></svg>BENEFITS</div>
<div class="pillar abs" style="left:345px">
  <svg width="60" height="46" viewBox="0 0 60 46"><circle cx="30" cy="10" r="8" fill="#fff"/><circle cx="12" cy="16" r="6" fill="#fff"/><circle cx="48" cy="16" r="6" fill="#fff"/><path d="M18 40 Q18 22 30 22 Q42 22 42 40Z" fill="#fff"/><path d="M2 40 Q2 26 12 26 Q18 26 19 30 L16 40Z" fill="#fff"/><path d="M58 40 Q58 26 48 26 Q42 26 41 30 L44 40Z" fill="#fff"/></svg>EMPLOYERS</div>
<div class="pillar abs" style="left:614px">
  <svg width="56" height="46" viewBox="0 0 56 46"><rect x="2" y="12" width="52" height="24" fill="#fff"/><circle cx="28" cy="24" r="8" fill="#1a5fae"/><rect x="26" y="19" width="4" height="10" fill="#fff"/><circle cx="9" cy="24" r="3" fill="#1a5fae"/><circle cx="47" cy="24" r="3" fill="#1a5fae"/></svg>PRICING</div>
<div class="pillar abs" style="left:884px">
  <svg width="40" height="50" viewBox="0 0 40 50"><path d="M8 16 Q8 4 20 4 Q33 4 33 15 Q33 22 25 26 Q22 28 22 34 L15 34 Q15 24 21 21 Q26 18 26 15 Q26 10 20 10 Q15 10 15 16Z" fill="#fff"/><rect x="14" y="38" width="9" height="9" fill="#fff"/></svg>QUESTIONS</div>

<section class="blog abs">
  <h2 class="abs">RECENT BLOG POSTS</h2>
  <svg class="arrows abs" width="48" height="28" viewBox="0 0 48 28"><polyline points="14,2 4,14 14,26" fill="none" stroke="#777" stroke-width="2.5"/><polyline points="34,2 44,14 34,26" fill="none" stroke="#777" stroke-width="2.5"/></svg>
  <article class="post abs" style="left:75px"><div class="ph" role="img" aria-label="Doctor consulting a woman patient at a desk" style="background:linear-gradient(120deg,#eef1f3,#c4ccd2)"></div><h3>Inventore Veritatis</h3><p>Lanventore veritatis et quasi architecto beatae vitae dicta sunt explicabo. Nemo enim ipsam voluptatem quia ..<a>Read More</a></p></article>
  <article class="post abs" style="left:435px"><div class="ph" role="img" aria-label="Nurse examining a little girl holding a toy" style="background:linear-gradient(120deg,#d9cfc6,#4f79b8)"></div><h3>Inventore Veritatis</h3><p>Lanventore veritatis et quasi architecto beatae vitae dicta sunt explicabo. Nemo enim ipsam voluptatem quia ..<a>Read More</a></p></article>
  <article class="post abs" style="left:795px"><div class="ph" role="img" aria-label="Doctor with clipboard talking to a male patient" style="background:linear-gradient(120deg,#eef2f4,#2f5f4c)"></div><h3>Inventore Veritatis</h3><p>Lanventore veritatis et quasi architecto beatae vitae dicta sunt explicabo. Nemo enim ipsam voluptatem quia ..<a>Read More</a></p></article>
</section>

<section class="subscribe abs">
  <div class="lbl abs">SUBSCRIBE EMAIL</div>
  <div class="field abs">Enter Email Address</div>
  <div class="go abs">SUBSCRIBE</div>
  <div class="follow abs">FOLLOW US</div>
  <div class="social abs"><i></i><i></i><i></i><i></i><i></i></div>
</section>

<footer class="footer">
  <div class="brand abs"><span class="dot"></span>Corvane Health</div>
  <p class="copy abs">Copyright © 2021, Company Name<br>All Right reserved</p>
  <div class="fcol abs" style="left:345px;top:3080px"><h4>QUICK LINKS</h4><ul><li>Home</li><li>About Us</li><li>Services</li><li>Employers</li><li>Pricing</li><li>FAQ'S</li><li>Blog</li><li>Contact Us</li></ul></div>
  <div class="fcol abs" style="left:536px;top:3080px"><h4>SERVICES</h4><ul><li>Services Overview</li><li>General Health Visits</li><li>Common Screening And Diagnostic Testing</li><li>Physical Exams</li><li>Specialized Treatments</li><li>Vaccinations</li><li>Additional Lab Testing</li><li>Telemedicine</li><li>Medical Imaging</li></ul></div>
  <div class="fcol contact abs" style="left:870px;top:3080px;width:260px"><h4>CONTACT INFO</h4><ul>
    <li style="line-height:21px;margin-top:6px"><svg width="10" height="14" viewBox="0 0 10 14"><path d="M5 0 Q10 0 10 5 Q10 8 5 14 Q0 8 0 5 Q0 0 5 0Z" fill="#222"/><circle cx="5" cy="5" r="2" fill="#fff"/></svg><span>14 Larkmoor Court, Suite 2,<br>Fenwick Bay, USA</span></li>
    <li><svg width="12" height="12" viewBox="0 0 12 12"><path d="M2 0 L5 3 L3.5 5 Q5 8 7 8.5 L9 7 L12 10 L10 12 Q2 11 0 2Z" fill="#222"/></svg><span>1-800-555-0142</span></li>
    <li><svg width="13" height="10" viewBox="0 0 13 10"><rect width="13" height="10" fill="#222"/><polyline points="0,0 6.5,6 13,0" fill="none" stroke="#fff" stroke-width="1.2"/></svg><span>hello@corvanehealth.example</span></li>
  </ul></div>
</footer>

</body>
</html>
```